quillfernPRESS is launching 2 new eBooks and needs beautiful and compelling cover designs and a desig

We are launching 2 non-fiction eBooks that are part of a series but will be launched separately, so we would like to see some continuity between the 2 designs - but each should have a strong stand alone identity.

The eBooks are both in the naturopathic/holistic health niche.

ebook 1 title is:
Shaping A Thriving Clinic
(sub) The Holistic Guide to building your own successful natural and
alternative therapy business.

The book is a comprehensive guide for naturopaths and other alternative health providers - ( Naturopath,
Nutritionist, Homeopath, Acupuncturist, Chiropractor,
Massage Therapist, or Holistic Health Specialist), who are seeking to setup their own, profitable naturopathic business.

ebook 2 title is:
Silver Pathways (subtitle) Get 30 + Clients in Under a Month

(sub/sub)32 ways to market your natural and alternative therapy business

This book is a list of 32 tips for the same audience to increase there customer referrals (and therefore income).

Each book should feature
written by Carla Whitmore
published by Whitmore Publishing

Each book should feature the authors photograph on the cover (attached) - no caveats on cropping etc - whatever fits with the design.

You can see more about the writer on her website here:

http://www.lakemeadowwellness.example.au/

What we require:

1) cover art for both eBooks that conforms to Kindle and iPad specs
2) Flat & 3D book cover art for use on website and marketing campaigns
3) we will require layered PSD files on completion of project.

I'd like to add that we are seeking to build a relationship with the designer we choose for this project, as we are publishing many other titles throughout 2014

Many eBook writers jump straight to Gigly for a cover. The result is most self published books have the same generic look the 'gigly' look.

I don't want that look.

We want to reward great design and ensure quillfernPRESS eBook titles have a great look.

The winning designer will be working with us on many more projects.

Martin Oakes
quillfernPRESS

```html
<!DOCTYPE html>
<html lang="en">
<head>
<meta charset="utf-8">
<title>Silver Pathways – eBook Cover</title>
<link href="https://fonts.googleapis.com/css2?family=Bebas+Neue&family=Oswald:wght@500;700&family=Parisienne&display=swap" rel="stylesheet">
<style>
  :root {
    --stage: #e9e9e4;
    --green-bright: #a6d30f;
    --green-pale: #c9e27c;
    --green-deep: #2f7a12;
    --green-ink: #2c6410;
    --title-yellow: #f7dc2f;
    --title-shadow: #8b8d7c;
    --sub-blue: #86dcec;
    --script-lime: #c6e466;
    --frame-white: #ffffff;
  }
  * { margin: 0; padding: 0; box-sizing: border-box; }
  html, body {
    width: 1200px; height: 850px; overflow: hidden;
    background: var(--stage);
  }
  .canvas { position: relative; width: 1200px; height: 850px; }

  .cover {
    position: absolute; left: 330px; top: 50px;
    width: 540px; height: 750px; overflow: hidden;
    background: var(--green-pale);
    box-shadow: 0 6px 24px rgba(0,0,0,.18);
  }
  .cover__panel-left {
    position: absolute; left: 0; top: 0; width: 250px; height: 100%;
    background: var(--green-bright);
  }
  .cover__frame {
    position: absolute; left: 14px; top: 14px; right: 14px; height: 560px;
    border-top: 4px solid var(--frame-white);
    border-right: 4px solid var(--frame-white);
  }
  .cover__band { position: absolute; left: 0; top: 0; width: 540px; height: 750px; }

  .cover__title {
    position: absolute; left: 30px; top: 40px;
    font-family: "Bebas Neue", "Oswald", sans-serif;
    font-size: 150px; line-height: .82;
    color: var(--title-yellow);
    text-shadow: -1px 1px 0 var(--title-shadow), -2px 2px 0 var(--title-shadow),
                 -3px 3px 0 var(--title-shadow), -4px 4px 0 var(--title-shadow),
                 -5px 5px 0 var(--title-shadow), -6px 6px 0 var(--title-shadow),
                 -7px 7px 0 var(--title-shadow);
  }
  .cover__subtitle {
    position: absolute; left: 30px; top: 318px;
    font-family: "Bebas Neue", "Oswald", sans-serif;
    font-size: 60px; line-height: .9;
    color: var(--sub-blue);
    text-shadow: -1px 1px 0 var(--title-shadow), -2px 2px 0 var(--title-shadow),
                 -3px 3px 0 var(--title-shadow), -4px 4px 0 var(--title-shadow);
  }
  .cover__tagline {
    position: absolute; left: 60px; top: 520px; width: 440px;
    font-family: "Parisienne", cursive;
    font-size: 34px; line-height: 1.15; text-align: center;
    color: var(--script-lime);
    transform: rotate(-12.4deg);
  }

  .cover__credits {
    position: absolute; right: 112px; top: 640px;
    font-family: "Oswald", sans-serif; text-align: right;
    color: var(--green-ink); line-height: 1;
  }
  .credits__label { font-size: 14px; font-weight: 500; letter-spacing: .5px; }
  .credits__name { font-size: 26px; font-weight: 700; margin: 2px 0 8px; }
  .cover__divider {
    position: absolute; left: 436px; top: 640px; width: 2px; height: 102px;
    background: var(--green-ink);
  }
  .cover__author-photo {
    position: absolute; left: 444px; top: 640px; width: 72px; height: 102px;
    background: linear-gradient(160deg, #d9cfc0 0%, #c7a57f 45%, #6e3b4b 100%);
  }
</style>
</head>
<body>
<main class="canvas">
  <section class="cover" aria-label="Silver Pathways eBook cover">
    <div class="cover__panel-left"></div>
    <div class="cover__frame"></div>

    <svg class="cover__band" viewBox="0 0 540 750" aria-hidden="true">
      <polygon points="0,730 540,610 540,632 0,752" fill="var(--green-bright)"/>
      <polygon points="0,560 540,440 540,612 0,732" fill="var(--green-deep)"/>
    </svg>

    <h1 class="cover__title">Silver<br>Pathways</h1>
    <p class="cover__subtitle">Get 30+ Clients<br>in Under a Month</p>
    <p class="cover__tagline">32 Ways to Market<br>your Natural and Alternative<br>Therapy Business</p>

    <div class="cover__credits">
      <div class="credits__label">WRITTEN BY</div>
      <div class="credits__name">CARLA WHITMORE</div>
      <div class="credits__label">PUBLISHED BY</div>
      <div class="credits__name">WHITMORE PUBLISHING</div>
    </div>
    <div class="cover__divider"></div>
    <div class="cover__author-photo" role="img" aria-label="Portrait photograph of author Carla Whitmore"></div>
  </section>
</main>
</body>
</html>
```